Redesign business cards

We have a new logo and I am not that happy with the layout of our existing card and looking for a change. Font is a bit small and the green can be hard to read. Logo may need a tidy up as the copy I have is not that hi-res too so require you to produce a hi-res version of the logo for us too. There will be three individual business cards to produce with just the names and phone numbers being different. Address will change too, but use what you see on the card for now.

Industry/Entity Type

Business

Requirements
Nice to have
• You could consider a redesign to the new logo, just not too radical. We like the blue and green hexagons as we feel that they are representative of oil industry that we are in.

```html
<!DOCTYPE html>
<html lang="en">
<head>
<meta charset="utf-8">
<title>Norvane Oil Services – Business Card</title>
<link href="https://fonts.googleapis.com/css2?family=Carlito:ital,wght@0,400;0,700;1,400;1,700&display=swap" rel="stylesheet">
<style>
  :root {
    --page-bg: #e9ebee;
    --card-bg: #ffffff;
    --brand-blue: #00aeef;
    --brand-green: #8dc63f;
    --light-blue: #6dcff6;
    --light-green: #c5e0a0;
    --text-grey: #8c8c8c;
  }
  html, body {
    margin: 0;
    padding: 0;
    width: 1200px;
    height: 1000px;
    overflow: hidden;
    background: var(--page-bg);
    font-family: "Carlito", "Calibri", sans-serif;
  }
  .business-card {
    position: absolute;
    left: 84px;
    top: 188px;
    width: 1032px;
    height: 624px;
    background: var(--card-bg);
    box-shadow: 0 6px 24px rgba(0, 0, 0, 0.12);
    overflow: hidden;
  }
  .hex-decoration {
    position: absolute;
    left: 500px;
    top: 0;
    width: 532px;
    height: 320px;
  }
  .brand-name {
    position: absolute;
    left: 46px;
    top: 160px;
    margin: 0;
    font-size: 124px;
    font-weight: 700;
    line-height: 1;
    color: var(--brand-blue);
    letter-spacing: -2px;
  }
  .brand-tagline {
    position: absolute;
    left: 48px;
    top: 284px;
    margin: 0;
    font-size: 52px;
    font-weight: 700;
    font-style: italic;
    line-height: 1;
    color: var(--text-grey);
  }
  .person {
    position: absolute;
    left: 46px;
    top: 370px;
  }
  .person-name {
    margin: 0;
    font-size: 46px;
    font-weight: 700;
    font-style: italic;
    line-height: 1;
    color: var(--brand-blue);
  }
  .person-role {
    margin: 8px 0 0 4px;
    font-size: 38px;
    font-weight: 700;
    font-style: italic;
    line-height: 1;
    color: var(--text-grey);
  }
  .person-credentials {
    margin: 10px 0 0 4px;
    font-size: 24px;
    line-height: 1;
    color: var(--text-grey);
  }
  .person-credentials em { font-style: italic; }
  .website {
    position: absolute;
    left: 48px;
    top: 540px;
    margin: 0;
    font-size: 40px;
    font-weight: 700;
    line-height: 1;
    color: var(--text-grey);
  }
  .contact {
    position: absolute;
    left: 516px;
    top: 370px;
    font-style: normal;
    color: var(--text-grey);
  }
  .contact-address {
    margin: 0;
    font-size: 40px;
    line-height: 48px;
  }
  .contact-phone,
  .contact-email {
    margin: 0;
    font-size: 40px;
    font-weight: 700;
    line-height: 48px;
  }
  .contact-phone { margin-top: 22px; }
</style>
</head>
<body>
  <div class="business-card">
    <svg class="hex-decoration" role="img" aria-label="Cluster of blue and green hexagon shapes" viewBox="0 0 532 320" xmlns="http://www.w3.org/2000/svg">
      <defs>
        <linearGradient id="hexTone" x1="0" y1="0" x2="1" y2="1">
          <stop offset="0" stop-color="#ffffff" stop-opacity="0"/>
          <stop offset="0.35" stop-color="#c5e0a0" stop-opacity="0.6"/>
          <stop offset="0.7" stop-color="#8dc63f" stop-opacity="0.55"/>
          <stop offset="1" stop-color="#6dcff6" stop-opacity="0.75"/>
        </linearGradient>
      </defs>
      <rect x="0" y="0" width="532" height="320" fill="url(#hexTone)"/>
    </svg>

    <h1 class="brand-name">Norvane</h1>
    <p class="brand-tagline">Oil Services</p>

    <div class="person">
      <p class="person-name">Daniel Ashford</p>
      <p class="person-role">Director</p>
      <p class="person-credentials">NZCE <em>(Mech)</em> P&amp;P</p>
    </div>

    <p class="website">www.norvane.com.au</p>

    <address class="contact">
      <p class="contact-address">417 Harbour Road<br>Kelvin Grove Q 4059</p>
      <p class="contact-phone">+61 400 318 742</p>
      <p class="contact-email">daniel@norvane.co.nz</p>
    </address>
  </div>
</body>
</html>
```